Table Tent Project for 50's Cafe

We need a graphic design which will be used on a table tent at a small 50's Cafe.

The restaurant is the Copper Kettle Cafe in Surrey, British Columbia, Canada.

Many photos can be found online at:
Friendbook: https://www.facebook.com/thecopperkettlecafe/
Snapgram: https://www.instagram.com/copperkettlecafe/

The purpose of this design is to create a table tent that informs customers about our social media presence.

Front: We would like it to include "Post a photo on Snapgram, Friendbook or Chirper and get 10% off your meal!" on the front.

Back: We would love to hear from you! Please take the time to review us online!

Thank you!

Industry/Entity Type

Restaurant

Requirements
Must have
• Please include the three Social Media icons (Friendbook, Snapgram, Chirper)
• Please keep the 50's theme.

```html
<!DOCTYPE html>
<html lang="en">
<head>
<meta charset="utf-8">
<title>Copper Kettle Cafe – Table Tent</title>
<link href="https://fonts.googleapis.com/css2?family=Fjalla+One&family=Oswald:wght@400;500&family=Rye&display=swap" rel="stylesheet">
<style>
  :root {
    --page: #efeae2;
    --paper: #e4cfa8;
    --paper-light: #f6ead2;
    --paper-dark: #cfae7e;
    --ink: #231c16;
    --red: #c41f26;
    --sepia: #8a7458;
    --sepia-soft: rgba(138,116,88,.35);
  }
  * { box-sizing: border-box; margin: 0; padding: 0; }
  html, body { width: 1200px; height: 800px; overflow: hidden; }
  body {
    background: var(--page);
    font-family: "Oswald", "Arial Narrow", sans-serif;
    color: var(--ink);
    position: relative;
  }
  .tent-card {
    position: absolute;
    top: 95px;
    width: 410px;
    height: 610px;
    background:
      radial-gradient(ellipse 70% 55% at 50% 42%, rgba(255,246,226,.95) 0%, rgba(246,234,210,.6) 35%, rgba(228,207,168,0) 70%),
      radial-gradient(circle at 50% 45%, var(--paper) 40%, var(--paper-dark) 100%);
    padding: 14px;
    box-shadow: 0 6px 18px rgba(0,0,0,.18);
  }
  .tent-card--back { left: 150px; }
  .tent-card--front { left: 640px; }
  .card-frame {
    position: relative;
    height: 100%;
    text-align: center;
    text-transform: uppercase;
  }
  .frame-lines {
    position: absolute; inset: 0; width: 100%; height: 100%;
    fill: none; stroke: var(--ink); pointer-events: none;
  }
  /* Back side */
  .review-copy {
    padding-top: 34px;
    font-family: "Fjalla One", "Oswald", sans-serif;
    font-size: 33px; line-height: 1.14; letter-spacing: .4px;
  }
  .review-copy .accent { color: var(--red); }
  .review-copy .gap { display: block; height: 10px; }
  .cafe-name {
    margin: 44px auto 0;
    display: inline-flex; align-items: center; gap: 10px;
    font-family: "Fjalla One", "Oswald", sans-serif;
    font-size: 28px; color: var(--ink);
  }
  .cafe-name .mark { width: 20px; height: 20px; background: var(--ink); }
  /* Footer shared */
  .card-footer {
    position: absolute; left: 24px; right: 24px; bottom: 24px;
    border-top: 1px solid var(--ink);
    padding-top: 10px;
  }
  .contact-row { display: flex; justify-content: center; align-items: center; gap: 10px; }
  .call-label { font-size: 10px; line-height: 1; text-align: left; font-weight: 500; }
  .phone { font-family: "Fjalla One", sans-serif; font-size: 22px; color: var(--red); }
  .divider { width: 1px; height: 32px; background: var(--ink); }
  .hours { font-size: 13px; line-height: 1.2; text-align: center; }
  .hours .red { color: var(--red); }
  .social-row {
    margin-top: 10px; padding-top: 6px;
    border-top: 1px solid var(--ink);
    display: flex; justify-content: space-between;
    font-size: 8.5px; letter-spacing: .3px;
  }
  /* Front side */
  .ribbon {
    margin: 24px auto 0; width: 300px; height: 44px;
    background: var(--ink); color: var(--paper-light);
    font-family: "Rye", serif; font-size: 21px; line-height: 46px;
    clip-path: polygon(0 0, 100% 0, 94% 50%, 100% 100%, 0 100%, 6% 50%);
  }
  .network-list { display: flex; justify-content: center; gap: 16px; margin-top: 10px; font-family: "Fjalla One", sans-serif; font-size: 14px; }
  .network-list li { list-style: none; display: flex; align-items: center; gap: 5px; }
  .network-list .dot { width: 14px; height: 14px; border-radius: 50%; background: var(--ink); }
  .photo-line { position: relative; height: 84px; margin: 10px 10px 0; }
  .photo-line .string { position: absolute; left: 0; right: 0; top: 8px; height: 1px; background: var(--ink); transform: rotate(1deg); }
  .photo-line .snaps { display: flex; justify-content: space-between; padding-top: 12px; }
  .photo-line .snap { width: 66px; height: 58px; background: linear-gradient(160deg, #c2ae90, var(--sepia)); border: 3px solid var(--paper-light); box-shadow: 0 2px 3px rgba(0,0,0,.25); }
  .snap:nth-child(1) { transform: rotate(-6deg); }
  .snap:nth-child(2) { transform: rotate(4deg); }
  .snap:nth-child(3) { transform: rotate(-3deg); }
  .snap:nth-child(4) { transform: rotate(5deg); }
  .snap:nth-child(5) { transform: rotate(-4deg); }
  .offer-heading { display: flex; justify-content: center; align-items: center; gap: 12px; margin-top: 8px; font-family: "Fjalla One", sans-serif; font-size: 31px; }
  .offer-heading .hand { width: 44px; height: 16px; background: linear-gradient(90deg, var(--sepia-soft), rgba(138,116,88,.15)); border-radius: 3px; }
  .offer-row { display: flex; justify-content: center; align-items: center; gap: 14px; margin-top: 4px; }
  .ornament-area {
    width: 92px; height: 124px; border-radius: 6px;
    background: linear-gradient(180deg, rgba(138,116,88,.12), rgba(138,116,88,.3), rgba(138,116,88,.12));
  }
  .discount-plate {
    width: 118px; height: 118px; border-radius: 50%;
    background: var(--ink); outline: 2px solid var(--paper-light); outline-offset: -9px;
    display: flex; align-items: center; justify-content: center;
    color: var(--red); font-family: "Fjalla One", sans-serif; font-size: 50px; line-height: 1;
  }
  .discount-plate small { font-size: 17px; display: inline-block; width: 26px; line-height: .95; text-align: left; }
  .offer-tail { font-family: "Fjalla One", sans-serif; font-size: 33px; margin-top: 4px; }
</style>
</head>
<body>
  <section class="tent-card tent-card--back" aria-label="Table tent back">
    <div class="card-frame">
      <svg class="frame-lines" viewBox="0 0 382 582" preserveAspectRatio="none" aria-hidden="true">
        <path vector-effect="non-scaling-stroke" stroke-width="3" d="M18 2H364A16 16 0 0 0 380 18V564A16 16 0 0 0 364 580H18A16 16 0 0 0 2 564V18A16 16 0 0 0 18 2Z"/>
        <path vector-effect="non-scaling-stroke" stroke-width="1" d="M22 9H360A13 13 0 0 0 373 22V560A13 13 0 0 0 360 573H22A13 13 0 0 0 9 560V22A13 13 0 0 0 22 9Z"/>
      </svg>
      <p class="review-copy">
        We would <span class="accent">love</span> to<br>hear from you!
        <span class="gap"></span>
        Please<br>take the time to<br>
        <span class="accent">Review us<br>online!</span>
      </p>
      <div class="cafe-name"><span class="mark"></span>Copper Kettle Cafe</div>
      <footer class="card-footer">
        <div class="contact-row">
          <span class="call-label">Call<br>us:</span>
          <span class="phone">(604) 555 0142</span>
          <span class="divider"></span>
          <span class="hours"><span class="red">Hours: 7.00AM - 5.00PM</span><br>7 days a week</span>
        </div>
        <div class="social-row">
          <span>Snapgram / copperkettlecafe</span>
          <span>Friendbook / thecopperkettlecafe</span>
          <span>Chirper</span>
        </div>
      </footer>
    </div>
  </section>

  <section class="tent-card tent-card--front" aria-label="Table tent front">
    <div class="card-frame">
      <svg class="frame-lines" viewBox="0 0 382 582" preserveAspectRatio="none" aria-hidden="true">
        <path vector-effect="non-scaling-stroke" stroke-width="3" d="M18 2H364A16 16 0 0 0 380 18V564A16 16 0 0 0 364 580H18A16 16 0 0 0 2 564V18A16 16 0 0 0 18 2Z"/>
        <path vector-effect="non-scaling-stroke" stroke-width="1" d="M22 9H360A13 13 0 0 0 373 22V560A13 13 0 0 0 360 573H22A13 13 0 0 0 9 560V22A13 13 0 0 0 22 9Z"/>
      </svg>
      <div class="ribbon">Post a photo on</div>
      <ul class="network-list">
        <li><span class="dot"></span>Snapgram</li>
        <li><span class="dot"></span>Friendbook</li>
        <li><span class="dot"></span>Chirper</li>
      </ul>
      <div class="photo-line">
        <span class="string"></span>
        <div class="snaps">
          <span class="snap" role="img" aria-label="Sepia photo of guests dining"></span>
          <span class="snap" role="img" aria-label="Sepia photo of guests dining"></span>
          <span class="snap" role="img" aria-label="Sepia photo of the diner interior"></span>
          <span class="snap" role="img" aria-label="Sepia photo of guests dining"></span>
          <span class="snap" role="img" aria-label="Sepia photo of guests dining"></span>
        </div>
      </div>
      <div class="offer-heading">
        <span class="hand" role="img" aria-label="Vintage pointing hand ornament"></span>
        And get
        <span class="hand" role="img" aria-label="Vintage pointing hand ornament"></span>
      </div>
      <div class="offer-row">
        <span class="ornament-area" role="img" aria-label="Swirl ornament and fork illustration"></span>
        <div class="discount-plate">10<small>% off</small></div>
        <span class="ornament-area" role="img" aria-label="Spoon illustration and swirl ornament"></span>
      </div>
      <p class="offer-tail">Your meal!</p>
      <footer class="card-footer">
        <div class="contact-row">
          <span class="call-label">Call<br>us:</span>
          <span class="phone">(604) 555 0142</span>
          <span class="divider"></span>
          <span class="hours"><span class="red">Hours: 7.00AM - 5.00PM</span><br>7 days a week</span>
        </div>
        <div class="social-row">
          <span>Snapgram / copperkettlecafe</span>
          <span>Friendbook / thecopperkettlecafe</span>
          <span>Chirper</span>
        </div>
      </footer>
    </div>
  </section>
</body>
</html>
```